Business Card Design

Im a small business that specialises in all aspects of sign installation, big and small, domestic and commercial. I have a construction and carpentry background. I'm after a professional looking business card, that has my logo as the forefront of the card incorporating the same colours as the my logo. No slogan as yet, but open to suggestions. The final design should communicate quality and class workmanship.

Target Market(s)

Managers and Owners of businesses

Industry/Entity Type

Small Business

Contact Information for Business Card

Carwyn Solbeck
Mob: 0417295036
Email: kto.fitouts@quillmail.net

Sign Installation
Property Improvement and Maintenance
Trade Services

Colors
dbdbdb
000000
ffffff

Requirements
Must have
• Logo
My name
My contact details
What I specialise in
Nice to have
• background image/images that are only just noticeable and do not take away from the logo or text.
Should not have
• No colours that contrast from my logo
No heavy machinery images to be used
Logo must stand out

```html
<!DOCTYPE html>
<html lang="en">
<head>
<meta charset="utf-8">
<title>KTO Installations – Business Card</title>
<link href="https://fonts.googleapis.com/css2?family=Open+Sans:ital,wght@0,400;0,700;1,400&display=swap" rel="stylesheet">
<style>
  :root {
    --ink: #000000;
    --paper: #ffffff;
    --silver: #dbdbdb;
    --brand-blue: #1f4e9c;
    --backdrop: #e9e9e9;
  }
  * { margin: 0; padding: 0; box-sizing: border-box; }
  html, body { width: 1200px; height: 900px; overflow: hidden; }
  body {
    background: var(--backdrop);
    font-family: "Open Sans", Arial, sans-serif;
    position: relative;
  }
  .card {
    position: absolute;
    left: 250px;
    width: 700px;
    height: 400px;
    overflow: hidden;
    box-shadow: 0 6px 18px rgba(0,0,0,0.25);
  }
  .card-back { top: 35px; background: var(--ink); }
  .card-back .emblem {
    position: absolute;
    left: 50%; top: 50%;
    width: 150px; height: 150px;
    margin: -75px 0 0 -75px;
    border: 12px solid var(--paper);
    border-radius: 50%;
  }
  .card-front { top: 465px; background: var(--paper); }
  .card-front .wave { position: absolute; inset: 0; }
  .brand {
    position: absolute;
    top: 55px; left: 0; right: 0;
    display: flex; align-items: center; justify-content: center; gap: 16px;
  }
  .brand-dot {
    width: 64px; height: 64px;
    border: 7px solid var(--brand-blue);
    border-radius: 50%;
  }
  .brand-name {
    color: var(--brand-blue);
    font-weight: 700;
    font-size: 42px;
    letter-spacing: 1px;
  }
  .services {
    position: absolute;
    left: 55px; top: 255px;
    list-style: none;
    color: var(--paper);
    font-style: italic;
    font-size: 20px;
    line-height: 31px;
  }
  .services li::before {
    content: "";
    display: inline-block;
    width: 11px; height: 11px;
    background: var(--paper);
    border-radius: 50%;
    margin-right: 9px;
    vertical-align: 2px;
  }
  .services li:nth-child(2) { margin-left: -5px; }
  .services li:nth-child(3) { margin-left: -10px; }
  .divider {
    position: absolute;
    left: 356px; top: 250px;
    width: 3px; height: 95px;
    background: var(--paper);
    border-radius: 2px;
  }
  .contact {
    position: absolute;
    right: 30px; top: 246px;
    text-align: right;
    color: var(--paper);
    font-size: 20px;
    line-height: 33px;
  }
  .contact .person { font-size: 25px; margin-bottom: 4px; }
  .contact svg { width: 16px; height: 16px; margin-left: 6px; vertical-align: -2px; }
</style>
</head>
<body>
  <section class="card card-back" aria-label="Card back">
    <div class="emblem"></div>
  </section>

  <section class="card card-front" aria-label="Card front">
    <svg class="wave" viewBox="0 0 700 400" preserveAspectRatio="none" aria-hidden="true">
      <path d="M0 140 C 150 175, 420 175, 700 160 L700 178 C 430 190, 160 190, 0 170 Z" fill="var(--silver)"/>
      <path d="M0 170 C 160 195, 430 192, 700 170 L700 400 L0 400 Z" fill="var(--ink)"/>
    </svg>

    <div class="brand">
      <div class="brand-dot"></div>
      <div class="brand-name">KTO INSTALLATIONS</div>
    </div>

    <ul class="services">
      <li>Sign Installation</li>
      <li>Property Improvement</li>
      <li>Maintenance Trade Services</li>
    </ul>

    <div class="divider"></div>

    <div class="contact">
      <div class="person">Carwyn Solbeck</div>
      <div class="phone">0417295036<svg viewBox="0 0 16 16" aria-hidden="true"><rect x="4" y="1" width="8" height="14" rx="1.5" fill="none" stroke="#fff" stroke-width="1.5"/></svg></div>
      <div class="email">kto.fitouts@quillmail.net<svg viewBox="0 0 16 16" aria-hidden="true"><rect x="1" y="3" width="14" height="10" fill="#fff"/><path d="M1 3 L8 9 L15 3" fill="none" stroke="#000" stroke-width="1.2"/></svg></div>
    </div>
  </section>
</body>
</html>
```